National hospice pharmacy network needs business cards

We need a business cards for a new company that is creating a network of independent pharmacies to provide medication delivery to hospice patients in their area. We will be providing them with logistics to build a delivery system, software to increase efficiency and the marketing to hospice agencies. The pharmacies will benefit with increasing their patient care, increasing their efficiency and increasing their profits.

the logo design is approved we are just darkening the colors. The logo will be updated when we have the final approval

Marketing

```html
<!DOCTYPE html>
<html lang="en">
<head>
<meta charset="utf-8">
<title>Hospiline business cards</title>
<link href="https://fonts.googleapis.com/css2?family=Didact+Gothic&display=swap" rel="stylesheet">
<style>
  :root {
    --backdrop: #e6e4df;
    --card: #f3f3f3;
    --brand-blue: #2b5aa0;
    --brand-green: #3aaa48;
    --pale-green: #c3e0c6;
    --ink: #3a3a3a;
    --font: "Didact Gothic", sans-serif;
  }
  * { margin: 0; padding: 0; box-sizing: border-box; }
  html, body { width: 1200px; height: 900px; overflow: hidden; }
  body {
    background: var(--backdrop);
    font-family: var(--font);
    position: relative;
  }
  .card {
    position: absolute;
    left: 300px;
    width: 600px;
    height: 388px;
    background: var(--card);
    overflow: hidden;
    box-shadow: 0 4px 14px rgba(0,0,0,0.12);
  }
  .card-front { top: 45px; }
  .card-back { top: 467px; }

  .front-mark {
    position: absolute;
    left: -120px;
    top: -150px;
    width: 360px;
    height: 360px;
    border-radius: 50%;
    background: var(--pale-green);
    opacity: 0.55;
  }
  .wordmark {
    position: absolute;
    display: flex;
    align-items: center;
    gap: 8px;
    color: var(--brand-blue);
    font-family: var(--font);
    font-weight: 400;
    letter-spacing: -0.5px;
    line-height: 1;
  }
  .wordmark .dot {
    display: inline-block;
    border-radius: 50%;
    background: var(--brand-green);
  }
  .card-front .wordmark { right: 70px; top: 160px; font-size: 46px; }
  .card-front .wordmark .dot { width: 16px; height: 16px; }
  .card-back .wordmark { left: 36px; top: 48px; font-size: 54px; }
  .card-back .wordmark .dot { width: 18px; height: 18px; }

  .contact {
    position: absolute;
    left: 300px;
    top: 120px;
    color: var(--ink);
    letter-spacing: 2px;
    font-size: 14px;
    line-height: 1.55;
  }
  .person-name { font-size: 14px; letter-spacing: 3px; text-transform: uppercase; }
  .person-role { color: var(--brand-green); font-size: 13px; letter-spacing: 2px; margin-bottom: 14px; }
  .address { margin-bottom: 14px; }
  .contact-list { list-style: none; }
  .contact-list li { display: flex; align-items: center; gap: 10px; }
  .contact-list svg { width: 12px; height: 12px; flex: none; }

  .edge-bands { position: absolute; left: 0; bottom: 0; width: 600px; height: 70px; }
</style>
</head>
<body>
  <section class="card card-front" aria-label="Card front">
    <div class="front-mark" aria-hidden="true"></div>
    <div class="wordmark">Hospiline<span class="dot"></span></div>
  </section>

  <section class="card card-back" aria-label="Card back">
    <div class="wordmark">Hospiline<span class="dot"></span></div>
    <div class="contact">
      <p class="person-name">Lukas Brenner</p>
      <p class="person-role">CEO</p>
      <p class="address">Lindenweg 12, 5401 Aarwil<br>Switzerland</p>
      <ul class="contact-list">
        <li>
          <svg viewBox="0 0 12 12" aria-hidden="true"><path d="M3 1h2l1 3-1.5 1a6 6 0 0 0 2.5 2.5L8 6l3 1v2c0 1-1 2-2 2A9 9 0 0 1 1 3c0-1 1-2 2-2z" fill="var(--brand-blue)"/></svg>
          +41 55 210 48 90
        </li>
        <li>
          <svg viewBox="0 0 12 12" aria-hidden="true"><rect x="3" y="0.5" width="6" height="11" rx="1" fill="none" stroke="var(--brand-blue)" stroke-width="1.2"/><circle cx="6" cy="9.5" r="0.7" fill="var(--brand-blue)"/></svg>
          +41 79 400 12 65
        </li>
        <li>
          <svg viewBox="0 0 12 12" aria-hidden="true"><rect x="0.5" y="2" width="11" height="8" fill="none" stroke="var(--brand-blue)" stroke-width="1.2"/><path d="M0.5 2l5.5 4.5L11.5 2" fill="none" stroke="var(--brand-blue)" stroke-width="1.2"/></svg>
          lukas@hospiline.com
        </li>
        <li>
          <svg viewBox="0 0 12 12" aria-hidden="true"><circle cx="6" cy="6" r="5.2" fill="none" stroke="var(--brand-blue)" stroke-width="1.2"/><path d="M0.8 6h10.4M6 0.8c-2.5 3-2.5 7.4 0 10.4M6 0.8c2.5 3 2.5 7.4 0 10.4" fill="none" stroke="var(--brand-blue)" stroke-width="0.9"/></svg>
          www.hospiline.com
        </li>
      </ul>
    </div>
    <svg class="edge-bands" viewBox="0 0 600 70" aria-hidden="true">
      <rect x="0" y="26" width="190" height="5" fill="var(--brand-green)"/>
      <path d="M170 70V48a20 20 0 0 1 20-20H600v42z" fill="var(--brand-blue)"/>
    </svg>
  </section>
</body>
</html>
```